Recycling Exhibition Web Design Project

We are developing a new website for a exhibition we have just taken over. The previous site is very basic and we require a complete redesign. The site should be designed to engage with and attract those who work in or provide services to the multibillion dollar wastes and recycling industry in the Asia pacific region. These will include Federal & State Governments, City councils, private sector, industry associations and other key bodies, education facilities.

KTLO is the premier waste and recycling event in the Asia Pacific region and known as place where the industry meets to share innovations, gain knowledge, to network and do business.
• Innovation
• Knowledge transfer
• Industry Networking
• Trade
Key point: need to reflect that 2012 show will attract large numbers of quality visitors from across wide range of the industry – city councils, facilities managers, etc

Site should deliver 3 key objectives.
1. Stimulate interest those who work in or provide services to the wastes and recycling industry by providing simple to access, relevant and topical information about the Expo, the Seminars, the Key Features, the sub activities and the key benefits to them.
2. Provide a platform that supports / improves EP by providing a range of interactive components – ie floor plan / video. In addition options for sales enquiries, registration, general feedback
3. Provide a way to highlight / showcase sponsors, show features and other key assets. (possibly a carousel above the fold)

We really like the dunmar website so a take on this could be good (http://www.dunmar-example.com.au/). Also we want to try to reinforce the brand so we should use the event as the hero image/banner.

Previous website - http://www.ktlo-example.com.au/

Target Market(s)

The site should be designed to engage with and attract those who work in or provide services to the multibillion dollar wastes and recycling industry

Industry/Entity Type

Recycling

Requirements
Must have
• The icons on the current site work quite well so inclusion as CTAs would be preferable.

Other key areas are

• Seminar Delegate & Visitor Registration
• Exhibitor Prospectus
• Floorplan
• Conference / Seminar content
• Social media + blog

Site visitors will need to feel like they are part of a community.
Site should reflect/display key industry stats & stats from 2011 expo

Please see the attached brief for more details and site map for menu items.

```html
<!DOCTYPE html>
<html lang="en">
<head>
<meta charset="utf-8">
<title>KTLO Waste &amp; Recycling Expo</title>
<link href="https://fonts.googleapis.com/css2?family=Ubuntu:wght@400;500;700&family=Open+Sans:wght@400;600&family=Crimson+Text:wght@600&display=swap" rel="stylesheet">
<style>
:root{
  --green:#3f8a2c;
  --green-dark:#2f6e22;
  --green-light:#5fa63f;
  --blue:#3f8fc9;
  --blue-dark:#1d6e9e;
  --text:#333;
  --muted:#777;
  --cream:#ece8dc;
  --page:#f6f4ef;
  --frame:#e6e1d6;
  --rule:#cfcabd;
  --ink:#1f1f1f;
}
*{box-sizing:border-box;margin:0;padding:0}
html,body{width:952px;height:1200px;overflow:hidden}
body{position:relative;background:#fff;font-family:"Open Sans",sans-serif;color:var(--text)}
.abs{position:absolute}
a{color:inherit;text-decoration:none}

.topnav{left:0;top:0;width:952px;height:31px;background:linear-gradient(#62ab43,#3c852a);border-bottom:1px solid #2f6e22}
.topnav a{position:absolute;top:9px;font-size:11px;color:#fff;font-family:"Ubuntu",sans-serif}
.topnav .active{top:4px;left:67px;width:52px;height:23px;line-height:21px;text-align:center;border:1px solid #cfe3c4;background:#8fbf77;color:#1f3c14}

.hero{left:0;top:31px;width:952px;height:408px;background:radial-gradient(ellipse at 60% 40%,#f6f3ea,var(--cream) 70%)}
.brand{display:flex;align-items:center;gap:10px}
.brand-dot{width:34px;height:34px;border-radius:50%;background:var(--green)}
.brand-name{font-family:"Crimson Text",serif;font-weight:600;color:var(--green);font-size:25px;line-height:1}
.hero .brand{left:66px;top:66px}
.tagline{left:60px;top:150px;width:340px;text-align:center;font-family:"Ubuntu",sans-serif;font-size:25px;line-height:33px;color:#444}
.tagline .b{color:var(--blue)}.tagline .g{color:var(--green)}
.rule-line{height:1px;background:linear-gradient(90deg,transparent,#b9b3a2,transparent)}
.intro{left:102px;top:256px;width:259px;font-size:10.5px;line-height:16.6px;color:#555;text-align:justify}
.intro .g{color:var(--green)}
.hero-photo{left:440px;top:104px;width:392px;height:300px;border-radius:40% 40% 20% 20%;background:radial-gradient(ellipse at 55% 45%,#2f6b45 0%,#2a5e3d 45%,#7aa54f 68%,rgba(236,232,220,0) 80%)}
.slider-tab{left:693px;top:419px;width:160px;height:20px;background:#fff;border-radius:12px 12px 0 0}
.slider-dots{left:704px;top:424px;display:flex;gap:4px}
.slider-dots span{width:13px;height:13px;border-radius:50%;background:#ddd8cb;font-size:8px;line-height:13px;text-align:center;color:#666}
.slider-dots .on{background:var(--green-light);color:#fff}
.slider-dots .pause{background:var(--blue);color:#fff}

.band{left:0;top:439px;width:952px;height:472px;background:var(--page)}

.datebox{left:22px;top:487px;width:42px;height:48px;background:var(--ink);color:#fff;text-align:center;font-family:"Ubuntu",sans-serif}
.datebox .d{font-size:22px;line-height:26px;margin-top:6px}
.datebox .m{font-size:9px;color:#bbb}
.count{left:22px;width:42px;height:16px;font-size:9px;color:#fff;display:flex;align-items:center;gap:10px;padding-left:7px}
.count.c1{top:541px;background:#1ea7d2}
.count.c2{top:563px;background:#8d8d8d}

.panel{background:var(--frame);border:1px solid #ddd7ca}
.panel .inner{position:absolute;left:7px;top:7px;right:7px;bottom:7px;background:#fff;border:1px solid #e0dbd0}
.dbl{position:absolute;height:4px;border-top:1px solid var(--rule);border-bottom:1px solid var(--rule)}
.h2{position:absolute;font-family:"Ubuntu",sans-serif;font-weight:500;color:var(--green-dark);font-size:19px}

.main{left:64px;top:451px;width:578px;height:646px}
.byline{left:90px;top:521px;font-size:8.5px;color:var(--muted)}
.byline b{color:#222;font-weight:600}
.post-photo{left:87px;top:549px;width:132px;height:125px;background:linear-gradient(#eef0f1 0%,#e5e6e6 55%,#9b7a5a 75%,#6c4f36 100%)}
.post-text{left:232px;top:547px;width:382px;font-size:9.6px;line-height:18.2px;color:#444}
.more{left:236px;top:656px;font-size:10px;font-weight:600;color:#222}
.pager{left:88px;top:700px;display:flex;gap:4px}
.pager span{height:17px;min-width:17px;padding:0 4px;border:1px solid #a7a290;font-size:8.5px;line-height:15px;text-align:center;color:#333}
.pager .lbl{color:#3a7ab4}
.pager .cur{background:#1ea7d2;color:#fff;border-color:#1ea7d2}
.lead{left:91px;top:807px;font-size:11px;font-weight:600;color:var(--green)}
.body-copy{left:91px;top:824px;width:532px;font-size:9.6px;line-height:17.4px;color:#333}
.prog{left:91px;width:320px;font-size:9.4px;line-height:17.4px;color:#333}
.prog h4{font-size:9px;font-weight:600;color:var(--green);letter-spacing:.3px}
.cta{left:413px;width:174px;height:52px;border-radius:10px;color:#fff;font-family:"Ubuntu",sans-serif;font-size:19px;padding-left:16px;display:flex;flex-direction:column;justify-content:center;line-height:19px;overflow:hidden}
.cta svg{position:absolute;right:10px;top:8px}
.cta.reg{top:889px;background:linear-gradient(#3a9fd6,var(--blue-dark))}
.cta.reg b{font-weight:700}
.cta.exh{top:972px;background:linear-gradient(#6db24a,#3b7f2a)}

.side{left:654px;top:451px;width:231px;height:394px}
.side .h2{left:0;width:100%;text-align:center}
.badge{position:absolute;left:25px;width:180px;border:2px solid #3b9a3b;background:#f2f8ef}
.view{position:absolute;left:26px;top:365px;font-size:10px;color:var(--green)}
.plan{left:654px;top:858px;width:231px;height:239px}
.plan-img{position:absolute;left:22px;top:68px;width:188px;height:141px;background:linear-gradient(135deg,#f4f4f2,#e8efe6 40%,#2f8a2f 41%,#2f8a2f 70%,#eeeeec 71%);border:1px solid #ddd}
.plan-link{position:absolute;left:20px;top:219px;font-size:10.5px;color:var(--green)}

.footer{left:0;top:1110px;width:952px;height:90px;background:#ebe7de;border-top:1px solid #d8d3c6}
.footer .brand{left:80px;top:16px}
.footer .brand-name{font-size:20px}
.footer .brand-dot{width:26px;height:26px}
.copy{left:340px;top:18px;width:350px;text-align:center;font-size:10.5px;line-height:19px;color:#333}
.copy a{color:var(--blue-dark)}
.follow{left:696px;top:30px;font-size:10.5px;color:#222;display:flex;align-items:center;gap:6px}
.follow i{display:block;width:21px;height:21px;border-radius:50%;background:#4d7cc0}
.follow i:nth-child(3){background:#5fb1d8}.follow i:nth-child(4){background:#2f79b0}.follow i:nth-child(5){background:#e8892a}
.grass{left:0;top:1176px;width:952px;height:24px;background:linear-gradient(#ebe7de,#9dc55a 40%,#6ea63a)}
</style>
</head>
<body>

<nav class="topnav abs">
  <a class="active" href="#">Home</a>
  <a style="left:136px" href="#">Conference Program</a>
  <a style="left:271px" href="#">Conference Presentations</a>
  <a style="left:431px" href="#">Free Workshop</a>
  <a style="left:536px" href="#">Welcome Reception</a>
  <a style="left:668px" href="#">Exhibitors</a>
  <a style="left:749px" href="#">Floor Plan</a>
  <a style="left:830px" href="#">Contact Us</a>
</nav>

<header class="hero abs">
  <div class="brand abs"><span class="brand-dot"></span><span class="brand-name">KTLO Waste &amp; Recycling Expo</span></div>
  <h1 class="tagline abs" style="font-weight:400"><span class="b">Recycling</span> Means a <span class="g">Better</span><br><span class="g">Future</span> for us all</h1>
  <div class="rule-line abs" style="left:96px;top:246px;width:266px"></div>
  <p class="intro abs"><span class="g">Recycling turns materials that would otherwise become waste into valuable resources.</span> Collecting used bottles, cans, and newspapers and taking them to the curb or to a collection facility is just the first in a series of steps hat generates a host of financial, environmental, and social returns.</p>
  <div class="rule-line abs" style="left:96px;top:363px;width:266px"></div>
  <div class="hero-photo abs" role="img" aria-label="Green recycling dumpster with a striped lid standing on grass among daisies"></div>
  <div class="slider-tab abs"></div>
  <div class="slider-dots abs"><span class="pause">II</span><span>1</span><span>2</span><span class="on">3</span><span>4</span><span>5</span><span>6</span><span>7</span></div>
</header>

<div class="band abs"></div>

<div class="datebox abs"><div class="d">09</div><div class="m">SEP</div></div>
<div class="count c1 abs"><svg width="9" height="8" viewBox="0 0 9 8"><ellipse cx="4.5" cy="3.5" rx="4.5" ry="3.3" fill="#fff"/></svg>0</div>
<div class="count c2 abs"><svg width="9" height="9" viewBox="0 0 9 9"><path d="M2 3a3 3 0 1 1 0 3" stroke="#fff" stroke-width="1.4" fill="none"/><path d="M0 1l3 1-2 2z" fill="#fff"/></svg>0</div>

<section class="main panel abs">
  <div class="inner"></div>
</section>
<div class="dbl" style="left:90px;top:467px;width:535px"></div>
<h2 class="h2" style="left:94px;top:481px">Coastal Climate Society Melbourne</h2>
<div class="abs" style="left:90px;top:511px;width:535px;height:1px;background:var(--rule)"></div>
<p class="byline abs">Written by <b>Daniel Rowe</b></p>
<div class="post-photo abs" role="img" aria-label="Person standing on top of a pile of flattened cardboard"></div>
<p class="post-text abs">Lorem Ipsum is simply dummy text of the printing and typesetting industry. Lorem Ipsum has been the industry's standard dummy text ever since the 1500s, when an unknown printer took a galley of type and scrambled it to make a type specimen book. It has survived not only five centuries, &nbsp;to make a type specimen book. It has survived not only five centuries,</p>
<p class="more abs">(more...) &nbsp;&nbsp;<svg width="13" height="8" viewBox="0 0 13 8"><path d="M0 0l4 4-4 4zM4.5 0l4 4-4 4zM9 0l4 4-4 4z" fill="#222"/></svg></p>
<div class="pager abs"><span class="lbl">Page 1 of 11</span><span class="cur">1</span><span>2</span><span>3</span><span>4</span><span>5</span><span>»</span><span>10</span><span>...</span><span>Last »</span></div>

<div class="dbl" style="left:90px;top:758px;width:535px"></div>
<h2 class="h2" style="left:90px;top:766px;width:480px;text-align:center">Conference Program</h2>
<div class="dbl" style="left:90px;top:792px;width:535px"></div>
<p class="lead abs">High quality conference. Low registration fee.</p>
<p class="body-copy abs">Prestigious industry experts discuss new legislation, technologies and innovations in resource recovery. This unique combination of quality content and subsidised registration fees will ensure all industry participants have access to the highest standard of information concerning critical issues facing our industry.</p>
<div class="prog abs" style="top:894px"><h4>CARBON PRICE &amp; CARBON FARMING INITIATIVE</h4>Thursday 10 November - Morning Conference<br>Only $185 (GST inc.). Registration fee includes lunch.</div>
<div class="prog abs" style="top:963px;width:330px"><h4>WASTE TO ENERGY &amp; LOCAL GOVERNMENT AWT PROCUREMENT</h4>Friday 11 November - Morning Conference. Only $99 (GST inc.)<br>GREEN BUILDINGS: DESIGN, CONSTRUCTION &amp; OPERATION</div>
<div class="prog abs" style="top:1033px;width:460px"><h4>PRODUCT STEWARDSHIP &amp; INNOVATION</h4>Thursday 10 November - Afternoon Conference (leads into free Welcome Reception 4-6pm)<br>Only $99 (GST inc.). Registration fee includes lunch.</div>

<a class="cta reg abs" href="#"><span>Register <b>Now</b></span><svg width="26" height="36" viewBox="0 0 26 36"><path d="M0 0h9l17 18-17 18H0l17-18z" fill="#fff" opacity=".85"/></svg></a>
<a class="cta exh abs" href="#"><span>Exhibitor<br>Prospectus</span><svg width="26" height="36" viewBox="0 0 26 36"><path d="M0 0h9l17 18-17 18H0l17-18z" fill="#fff" opacity=".85"/></svg></a>

<aside class="side panel abs">
  <div class="inner"></div>
  <div class="dbl" style="left:24px;top:14px;width:186px"></div>
  <h2 class="h2" style="top:30px">Supported By</h2>
  <div class="abs" style="left:24px;top:57px;width:186px;height:1px;background:var(--rule)"></div>
  <div class="badge" style="top:71px;height:55px"></div>
  <div class="badge" style="top:139px;height:51px"></div>
  <div class="badge" style="top:204px;height:68px"></div>
  <div class="badge" style="top:284px;height:73px"></div>
  <a class="view" href="#">View more &nbsp;<svg width="9" height="7" viewBox="0 0 9 7"><path d="M0 0l3.5 3.5L0 7zM4.5 0L8 3.5 4.5 7z" fill="var(--green)"/></svg></a>
</aside>

<aside class="plan panel abs">
  <div class="inner"></div>
  <div class="dbl" style="left:24px;top:15px;width:186px"></div>
  <h2 class="h2" style="left:0;width:100%;text-align:center;top:33px">Floor Plan</h2>
  <div class="abs" style="left:24px;top:60px;width:186px;height:1px;background:var(--rule)"></div>
  <div class="plan-img" role="img" aria-label="Expo hall floor plan with green exhibitor stands"></div>
  <a class="plan-link" href="#">Click here to receive 2012 floor plan &nbsp;<svg width="9" height="7" viewBox="0 0 9 7"><path d="M0 0l3.5 3.5L0 7zM4.5 0L8 3.5 4.5 7z" fill="var(--green)"/></svg></a>
</aside>

<footer class="footer abs">
  <div class="brand abs"><span class="brand-dot"></span><span class="brand-name">KTLO Waste &amp; Recycling Expo</span></div>
  <p class="copy abs">Copyright © 2012, KTLO Waste &amp; Recycling Expo<br>Contact us at : <a href="#">info@ktlo-example.com.au</a></p>
  <div class="follow abs"><span>Follow Us On :</span><i></i><i></i><i></i><i></i></div>
</footer>
<div class="grass abs" role="img" aria-label="Strip of green grass along the bottom edge"></div>

</body>
</html>
```